Motivational Quotes Poster Series

This is a 3 poster design series for Ridgeway Haul Academy. The size of each poster should be 18 inches wide and 24 inches tall. The goal of these posters is to serve as motivational "signs" to be hung in the office area for the employees (not customers). These employees are instructors/teachers, teaching students how to drive semi trucks. While each design is a separate poster and design, we're posting as 1 project because we'd like some continuity between the series. Below we'll break down the details of all 3 posters...

Poster #1
Text that must appear on poster - "If You Want The Best Out Of Each Student" and "Give The Best Of You!" Note: While this text must appear on the poster, you can arrange in the layout as you see fit. For example, first line could be at top of poster and second line on bottom.

Poster #2
Text that must appear on poster - "Invest In People" and "Change Someone's Life" (same notes apply as in 1st poster)

Poster #3
Text that must appear on poster - "Today Is..." and "Just Another Day For You" and "The Most Important Day In Their Life" Note: This can be laid out on the poster however you see fit, but each phrase needs to be separate and it needs to flow.

Target Market(s)

Truck Driver Training Instructors - These are middle-aged, mostly male, masculine type personalities.

Industry/Entity Type

Training

Requirements
Must have
• Must have noted text from description
Must have working files (ie - PSD, EPS, AI, etc) provided
Must have common theme between each poster in series
Must have easy to read font and layout
Must have product dimensions of 18 inches (width) by 24 inches (height). If design uses full dimensions please include quarter inch bleed.
Nice to have
• Nice to have a trucking theme...related to trucking industry, but not over the top. Example - This could mean subtle injection of background tire tracks, but by no means are tire tracks required.

For inspiration, you can visit the site at http://www.ridgewayhaulacademy.com. While you can use the colors of the site/logo, you can still branch out between each poster to try new colors within reason.

Note: While we've attached the logo to this project, it COULD be used but doesn't HAVE to be included in the design. The logo IS NOT a focal point. The phrases in the poster ARE the focal point.

```html
<!DOCTYPE html>
<html lang="en">
<head>
<meta charset="utf-8">
<title>Ridgeway Haul Academy – Motivational Poster Series</title>
<link rel="stylesheet" href="https://fonts.googleapis.com/css2?family=Jost:wght@600;700&display=swap">
<style>
  :root {
    --backdrop: #f4f4f4;
    --poster-light: #ffffff;
    --poster-shade: #e3e3e3;
    --accent-red: #d0101c;
    --text-grey: #3c3c3c;
  }
  html, body {
    margin: 0;
    padding: 0;
    width: 1200px;
    height: 849px;
    overflow: hidden;
    background: var(--backdrop);
  }
  .series {
    position: relative;
    width: 1200px;
    height: 849px;
    font-family: "Jost", "Century Gothic", sans-serif;
  }
  .poster {
    position: absolute;
    top: 245px;
    width: 293px;
    height: 390px;
    background: radial-gradient(ellipse 70% 55% at 50% 40%, var(--poster-light) 0%, #f6f6f6 45%, var(--poster-shade) 100%);
    overflow: hidden;
  }
  .poster--student { left: 134px; }
  .poster--invest { left: 454px; }
  .poster--today { left: 773px; }

  .headline {
    position: absolute;
    left: 18px;
    margin: 0;
    color: var(--accent-red);
    font-weight: 700;
    font-size: 38px;
    line-height: 41px;
    text-transform: uppercase;
    letter-spacing: -1px;
    white-space: nowrap;
  }
  .subline {
    position: absolute;
    left: 18px;
    margin: 0;
    color: var(--text-grey);
    font-weight: 600;
    font-size: 18px;
    line-height: 20px;
    text-transform: uppercase;
    letter-spacing: -0.4px;
    white-space: nowrap;
  }

  .poster--student .headline { top: 50px; }
  .poster--student .subline { top: 228px; }

  .poster--invest .headline { top: 46px; font-size: 50px; line-height: 48px; }
  .poster--invest .subline { top: 166px; }

  .poster--today .lead-in { top: 54px; }
  .poster--today .headline { top: 87px; }
  .poster--today .subline.closing { top: 262px; }

  .academy-name {
    position: absolute;
    right: 12px;
    bottom: 8px;
    margin: 0;
    color: var(--accent-red);
    font-weight: 700;
    font-size: 9px;
    text-transform: uppercase;
  }
</style>
</head>
<body>
<main class="series">
  <article class="poster poster--student">
    <h2 class="headline">If you want<br>the best out<br>of each<br>student</h2>
    <p class="subline">Give the best of you!</p>
    <p class="academy-name">Ridgeway Haul Academy</p>
  </article>

  <article class="poster poster--invest">
    <h2 class="headline">Invest in<br>people</h2>
    <p class="subline">Change someone’s life</p>
    <p class="academy-name">Ridgeway Haul Academy</p>
  </article>

  <article class="poster poster--today">
    <p class="subline lead-in">Today is...</p>
    <h2 class="headline">Just<br>another<br>day for<br>you</h2>
    <p class="subline closing">The most important<br>day in their life</p>
    <p class="academy-name">Ridgeway Haul Academy</p>
  </article>
</main>
</body>
</html>
```